Simple Wordpress "Coming soon" style website (1-3 sections) for a new games company.

This should be a relatively simple, but high-quality website, as it's only intended to be a placeholder for a later more complete website. 47K22P SEZC is a newly-established multi-platform games development company based in the Caribbean. We have a company logo. The logo is only three-colour and uses the Adobe Trajan font. Our business cards also use Adobe Georgia font for email/web addresses and phone numbers, as the Trajan font is capitals only. Our tagline is "Where Games Are Reimagined". Our first app, "Zorb", is in the final stages of development but it's not ready, so we need a "coming soon" style landing (splash) page, with "About Us", "Contact Us" and "Product Timeline" details. We have a Zorb product logo that can be included with the details, plus a screenshot of an in-progress game. The site design needs to allow for multilingual content. It doesn't require a translation plugin, as we've provided the "About Us" and "Product Timeline" content in 16 languages. The only contact details will be the email address. Examples of similar products / companies (if that helps) are "Dab The Tiles / Brinwell", "Jolly Shade / Q-Drift", and "Grid Sketch / CalmLoop". Please note that, with reference to the final selected design, we will need the ability to edit the content, as friends in all 15 countries will be supplying us with colloquially edited versions of the welcome blurb, and we can quickly supply replacement photographic imagery for any backgrounds or POS material. Please ask if you need any further information.
Target Market(s)
18-44yo puzzle gamers (40% male - 60% female)
Industry/Entity Type
Computer games industry
Coding
Coded - Design and coding required
Number of Pages Required
1 page
Font styles to use
Other font styles liked:
- See description
Look and feel

```html
<!DOCTYPE html>
<html lang="en">
<head>
<meta charset="utf-8">
<title>47K22P SEZC – Where Games Are Reimagined</title>
<link rel="stylesheet" href="https://fonts.googleapis.com/css2?family=Cinzel:wght@400;500;600&family=Kumbh+Sans:wght@400;500;700;800&display=swap">
<style>
:root{
  --night-top:#18233a;
  --night-mid:#1f2d3f;
  --night-low:#141c2b;
  --ink:#ffffff;
  --soft:#e8ecf3;
  --blue:#6e8ff3;
  --teal:#10b7bc;
  --pink:#f65fa3;
  --coral:#f8695a;
  --green:#27a04a;
  --device:#f4f4f4;
}
*{margin:0;padding:0;box-sizing:border-box}
html,body{width:1200px;height:807px;overflow:hidden}
body{
  position:relative;
  font-family:"Kumbh Sans",sans-serif;
  color:var(--ink);
  background:
    radial-gradient(ellipse 520px 300px at 560px 470px, rgba(70,110,130,.35), transparent 70%),
    radial-gradient(ellipse 400px 260px at 1050px 120px, rgba(60,80,110,.35), transparent 70%),
    linear-gradient(180deg,var(--night-top) 0%,var(--night-mid) 45%,var(--night-low) 100%);
}
.site-header{position:absolute;left:0;top:0;width:1200px;height:100px}
.brand{position:absolute;left:113px;top:18px;display:flex;align-items:center;gap:10px}
.brand-mark{width:40px;height:40px;border-radius:50%;background:#fff}
.brand-name{font-family:"Kumbh Sans",sans-serif;font-weight:700;font-size:22px;color:var(--ink);letter-spacing:.5px}
.main-nav{position:absolute;left:448px;top:44px;display:flex;gap:32px;font-size:14px;letter-spacing:.4px;font-weight:500}
.main-nav a{color:var(--ink);text-decoration:none}
.mail{position:absolute;left:846px;top:43px;display:flex;align-items:center;gap:8px;font-size:14px}
.lang{position:absolute;left:990px;top:32px;width:96px;height:40px;border:1px solid var(--ink);border-radius:20px;display:flex;align-items:center;justify-content:center;gap:7px;font-size:11px;font-weight:500}
.hero-title{position:absolute;left:114px;top:128px;font-family:"Cinzel",serif;font-weight:500;font-size:41px;line-height:46px;letter-spacing:.6px}
.hero-copy{position:absolute;left:114px;top:283px;width:392px;font-size:13px;line-height:19.7px;color:var(--soft)}
.hero-copy p+p{margin-top:9px}
.name-inline{font-weight:700;color:var(--teal)}
.device{position:absolute;left:599px;top:155px;width:487px;height:346px;background:var(--device);border-radius:16px;box-shadow:0 4px 12px rgba(0,0,0,.35)}
.device-btn{position:absolute;left:10px;top:164px;width:20px;height:20px;border:1px solid #ccc;border-radius:50%}
.device-cam{position:absolute;right:20px;top:170px;width:4px;height:4px;border-radius:50%;background:#333}
.device-screen{position:absolute;left:41px;top:20px;width:406px;height:306px;
  background:linear-gradient(90deg,#e8e8e8 0 7%,#d9c9d6 7%,#e9b9c8 25%,#f2d08a 50%,#b9c3cf 75%,#e2e2e2 93%,#c06a2e 93%,#3e7fb0 97%,#f0f0f0 100%)}
.timeline-title{position:absolute;left:112px;top:524px;font-size:28px;font-weight:500;display:flex;gap:10px}
.timeline-title .name-inline{font-weight:700}
.timeline{position:absolute;left:0;top:575px;width:1200px;height:160px}
.track{position:absolute;left:120px;top:103px;width:940px;height:2px;background:var(--ink)}
.milestone{position:absolute;top:0;width:120px;margin-left:-60px;text-align:center}
.bubble{position:relative;width:69px;height:69px;margin:7px auto 0;border-radius:50%;display:flex;align-items:center;justify-content:center;font-weight:800;font-size:14px;letter-spacing:.4px;box-shadow:-6px 8px 0 -1px rgba(40,48,64,.85),6px 8px 0 -1px rgba(40,48,64,.85)}
.stem{width:2px;height:22px;margin:0 auto;background:var(--ink)}
.dot{width:12px;height:12px;margin:-1px auto 0;border-radius:50%;border:2px solid var(--ink)}
.label{margin-top:9px;font-size:14px;line-height:18px}
.blue .bubble,.blue .dot{background:var(--blue)}
.teal .bubble,.teal .dot{background:var(--teal)}
.pink .bubble,.pink .dot{background:var(--pink)}
.coral .bubble,.coral .dot{background:var(--coral)}
.site-footer{position:absolute;left:0;top:766px;width:1200px;height:41px;background:var(--green);display:flex;align-items:center;justify-content:center;font-size:13px}
</style>
</head>
<body>
<header class="site-header">
  <div class="brand"><span class="brand-mark"></span><span class="brand-name">47K22P SEZC</span></div>
  <nav class="main-nav"><a href="#about">ABOUT US</a><a href="#contact">CONTACT US</a><a href="#timeline">PRODUCT TIMELINE</a></nav>
  <div class="mail">
    <svg width="15" height="11" viewBox="0 0 15 11"><rect x=".5" y=".5" width="14" height="10" fill="none" stroke="#fff"/><path d="M.5 .5 7.5 6 14.5 .5M.5 10.5 5.5 5M14.5 10.5 9.5 5" fill="none" stroke="#fff"/></svg>
    <span>info@47k22p.ky</span>
  </div>
  <div class="lang">
    <svg width="25" height="16" viewBox="0 0 25 16"><rect width="25" height="16" fill="#fff"/><g fill="#d22"><rect y="0" width="25" height="2"/><rect y="4" width="25" height="2"/><rect y="8" width="25" height="2"/><rect y="12" width="25" height="2"/></g><rect width="11" height="8" fill="#2b3a8c"/></svg>
    <span>ENG</span>
    <svg width="7" height="5" viewBox="0 0 7 5"><path d="M.5 .5 3.5 4 6.5 .5" fill="none" stroke="#fff"/></svg>
  </div>
</header>

<main>
  <h1 class="hero-title">47K22P SEZC -<br>WHERE GAMES<br>ARE REIMAGINED</h1>
  <div class="hero-copy" id="about">
    <p>Get ready to embark on an exhilarating journey with 47K22P SEZC, a dynamic, multi-platform game development company born in the heart of the Caribbean! Our diverse team hails from around the world, blending talent with passion. From fresh graduates to industry veterans, we've united under one vision: to radically reimagine existing games.</p>
    <p>With our debut title " <span class="name-inline">Zorb</span> " a captivating Colouring-In/PBN game for Fonix, Droidel, Maxen, and PC, we're set to showcase what true innovation looks like. Stay tuned to see how we're reshaping the gaming landscape, one Pixel at a time!</p>
  </div>

  <div class="device">
    <span class="device-btn"></span>
    <div class="device-screen" role="img" aria-label="In-progress game screenshot: a colourful bird illustration with tool icons on the left and numbered colour swatches on the right"></div>
    <span class="device-cam"></span>
  </div>

  <h2 class="timeline-title" id="timeline"><span class="name-inline">Zorb</span><span>Timeline</span></h2>
  <section class="timeline">
    <div class="track"></div>
    <div class="milestone blue" style="left:173px"><div class="bubble">Q3-23</div><div class="stem"></div><div class="dot"></div><div class="label">Zorb<br>conceived</div></div>
    <div class="milestone teal" style="left:316px"><div class="bubble">Q4-23</div><div class="stem"></div><div class="dot"></div><div class="label">Proof of<br>concept</div></div>
    <div class="milestone pink" style="left:462px"><div class="bubble">Q1-24</div><div class="stem"></div><div class="dot"></div><div class="label">Working game<br>(PC only)</div></div>
    <div class="milestone coral" style="left:601px"><div class="bubble">Q2-24</div><div class="stem"></div><div class="dot"></div><div class="label">Team gathering<br>&amp; pitch</div></div>
    <div class="milestone blue" style="left:742px"><div class="bubble">Q3-24</div><div class="stem"></div><div class="dot"></div><div class="label">47K22P<br>established</div></div>
    <div class="milestone teal" style="left:884px"><div class="bubble">Q4-24</div><div class="stem"></div><div class="dot"></div><div class="label">Zorb<br>Completed</div></div>
    <div class="milestone pink" style="left:1027px"><div class="bubble">Q1-25</div><div class="stem"></div><div class="dot"></div><div class="label">Zorb<br>launched!</div></div>
  </section>
</main>

<footer class="site-footer" id="contact">© 2024 FortysevenK22P . All Rights Reserved.</footer>
</body>
</html>
```